Structural Engineering Business Card

Orvik Drafting does residential house plans for clients in Central Florida. Would like simple but elegant business card that is appropriate for a house plan engineering company. Prefer black business card with black/white them but open to other shades of blue. I uploaded a sample card that I came across that looked good but please come up with your own creative designs.

Contact Information for Business Card

Name, Title, Phone, Email, Address, website

```html
<!DOCTYPE html>
<html lang="en">
<head>
<meta charset="utf-8">
<title>Orvik Drafting – Business Card</title>
<link href="https://fonts.googleapis.com/css2?family=Montserrat:wght@400;500;700;800&display=swap" rel="stylesheet">
<style>
  :root{
    --stage:#b4b4b4;
    --card:#262626;
    --accent:#4ec3e6;
    --logo-grey:#8a8a8a;
    --text:#e6e6e6;
    --drawing-a:#3a3a3a;
    --drawing-b:#2b2b2b;
  }
  html,body{margin:0;padding:0;width:1200px;height:900px;overflow:hidden;background:var(--stage);}
  body{font-family:"Montserrat",sans-serif;display:flex;flex-direction:column;align-items:center;justify-content:center;gap:50px;}
  .card{
    position:relative;width:665px;height:380px;background:var(--card);
    border-radius:26px;box-shadow:0 5px 0 var(--accent);overflow:hidden;
  }
  .house-drawing{
    position:absolute;left:34px;bottom:34px;width:300px;height:250px;border-radius:6px;
    background:radial-gradient(ellipse at 50% 60%, var(--drawing-a), var(--drawing-b) 75%);
  }
  .card-back .house-drawing{left:40px;width:340px;height:280px;bottom:40px;}
  .brand{
    display:flex;align-items:center;gap:10px;
    font-weight:800;color:var(--logo-grey);text-transform:uppercase;letter-spacing:1px;
  }
  .brand-mark{width:16px;height:16px;background:var(--accent);}
  .card-front .brand{position:absolute;right:44px;top:44px;font-size:30px;}
  .card-back .brand{position:absolute;right:46px;top:50%;transform:translateY(-50%);font-size:40px;flex-direction:column;align-items:flex-end;gap:14px;line-height:1.05;text-align:right;}
  .card-back .brand-mark{width:22px;height:22px;}
  .details{position:absolute;left:370px;top:120px;color:var(--text);}
  .person-name{margin:0;color:var(--accent);font-weight:700;font-size:26px;}
  .person-title{margin:2px 0 18px;font-size:14px;}
  .address{font-style:normal;font-size:14px;line-height:1.35;margin-bottom:16px;}
  .contact-list{list-style:none;margin:0;padding:0;font-size:14px;line-height:1.55;}
  .contact-list li{display:flex;align-items:center;gap:10px;}
  .contact-list svg{width:13px;height:13px;fill:var(--accent);flex:none;}
</style>
</head>
<body>
  <section class="card card-front">
    <div class="house-drawing" role="img" aria-label="Line drawing of a two-storey house elevation with dimension lines"></div>
    <div class="brand"><span class="brand-mark"></span>Orvik Drafting</div>
    <div class="details">
      <h1 class="person-name">Daniel Reyes</h1>
      <p class="person-title">Owner</p>
      <address class="address">Lindenweg 42<br>32801 Orlando</address>
      <ul class="contact-list">
        <li><svg viewBox="0 0 24 24"><path d="M6.6 10.8a15.1 15.1 0 0 0 6.6 6.6l2.2-2.2a1 1 0 0 1 1-.25 11.4 11.4 0 0 0 3.6.57 1 1 0 0 1 1 1V20a1 1 0 0 1-1 1A17 17 0 0 1 3 4a1 1 0 0 1 1-1h3.5a1 1 0 0 1 1 1c0 1.25.2 2.45.57 3.57a1 1 0 0 1-.25 1z"/></svg>+1 407 555 0182</li>
        <li><svg viewBox="0 0 24 24"><path d="M2 5h20v14H2zm2 2v.5l8 5 8-5V7l-8 5z"/></svg>hello@orvikdrafting.com</li>
        <li><svg viewBox="0 0 24 24"><path d="M12 2a10 10 0 1 0 0 20 10 10 0 0 0 0-20zm0 2c1 1.3 1.8 3 2.1 5H9.9C10.2 7 11 5.3 12 4zM4.3 11h3.6a15 15 0 0 0 0 2H4.3a8 8 0 0 1 0-2zm5.6 2a13 13 0 0 1 0-2h4.2a13 13 0 0 1 0 2zm6.2 0a15 15 0 0 0 0-2h3.6a8 8 0 0 1 0 2zM12 20c-1-1.3-1.8-3-2.1-5h4.2c-.3 2-1.1 3.7-2.1 5z"/></svg>www.orvikdrafting.com</li>
      </ul>
    </div>
  </section>

  <section class="card card-back">
    <div class="house-drawing" role="img" aria-label="Line drawing of a house front elevation with porch and dimension lines"></div>
    <div class="brand"><span class="brand-mark"></span><span>Orvik<br>Drafting</span></div>
  </section>
</body>
</html>
```